Design Creative Banner or Gif Ads. 3 Designs To Be Selected

Come up with some creative banner ads for stonewell.co.nz

*At least 3 different winning banners will be chosen*

Please provide banner ads / gif ads in common google ads / website banner formats.

They can be gif or static but must stand out while still maintaining clear clean text and visuals, with a premium professional feel (please avoid clip art or anything that gives a cheap message).

Please keep in mind that these will likely be small ads so text needs to be large and if there's there a lot of text then use multiple frames/ pages as submit as a gif.

Style
Minimal & clean lines
Architectural or realistic images
Avoid cartoon styles, clipart, or anything that looks cheap

Font
Nexa or Montserrat or similar

Tone
Premium, serious, trustworthy — fits new builds

Colours
Option 1: Deep Navy (trust & quality) & lighter blues and warm grey
Option 2: Open to bright colours to help the ads stand out, such as (but not limited to) bright pink with black, yellow, fluorescent green, provided the messaging is still done professionally.
Our logo is attached (Stone Well Logo)

Display Sizes
Ad specs for file sizes should be file formats like JPEG, GIF, and PNG, with animations limited to a max of 30 seconds or less.
We will need several different ad sizes provided for each of the 3 selected winning designs.

• Medium Rectangle: 300 × 250 pixels
• Leaderboard: 728 × 90 pixels
• Desktop Banner ad image: (640x360 pixels)
• Desktop Banner ad image 2: (300x600 pixels)
• Possibly one or two other sizes

Flexibility to be creative
The ad text, words, upper/lower case, layout, colour, theme, and images can be adjusted to how you think it will look best. The follow example ads are just examples of what we are after but we are keen to see what you can create.

Recommendations at this point:
1. Avoid text heavy
2. Looking for more Gif ads
3. Imaging: if possible use real stock photo's rather than AI

Themes:

1
Building Soon? Start Here
Free Build Planning Pack:
✓ Build Cost Calculator
✓ Hidden Cost Checklist
✓ Builder Comparison Guide
Build With Confidence
Download Free

2
Before You Choose A Builder
Compare Price, Scope, Risk & Value
Avoid Costly Mistakes
Choose The Right Builder With Confidence
Download The Free Guide

3
Planning A New Build?
Avoid These Common Mistakes:
✗ Hidden Exclusions
✗ Missing Scope
✗ Unrealistic Allowances
✗ Budget Blowouts
Download The Free Guide

4
Before You Buy Land
Know what it could cost to build.
Avoid Costly Building Mistakes
Download Our Free Guides

5
Know Your Build Budget?
• Free Build Cost Calculator
• Hidden Cost Checklist
• Build Planning Tools
Calculate Costs (Download)

Target Market(s)

Landowners looking to build

Industry/Entity Type

Building

Font styles to use
Other font styles liked:
• Nexa or Montserrat or similar

Requirements
Should not have
• Avoid cartoon styles, clipart, or anything that looks cheap

```html
<!DOCTYPE html>
<html lang="en">
<head>
<meta charset="utf-8">
<title>Stone Well – Display Ads</title>
<link rel="stylesheet" href="https://fonts.googleapis.com/css2?family=Montserrat:wght@400;500;600;700&family=Source+Sans+3:wght@400&display=swap">
<style>
  :root{
    --board:#d2d3d5;
    --panel:#f4f5f6;
    --panel-edge:#ffffff;
    --sky-blue:#2a9fc9;
    --navy:#0f3350;
    --ink:#333a40;
    --ink-soft:#444a50;
    --cross:#e3262b;
    --btn-top:#2a86b4;
    --btn-bottom:#196a96;
    --label:#1c1c1c;
  }
  *{box-sizing:border-box;margin:0;padding:0}
  html,body{width:1200px;height:1060px;overflow:hidden;background:var(--board)}
  body{position:relative;font-family:'Montserrat',Arial,sans-serif;color:var(--ink)}

  .size-label{position:absolute;font-family:'Source Sans 3',Arial,sans-serif;font-size:17px;color:var(--label)}

  .ad{position:absolute;overflow:hidden;
    background:radial-gradient(ellipse at 70% 40%,#ffffff 0%,var(--panel) 55%,#eceeef 100%)}

  .sketch{position:absolute;
    background:linear-gradient(180deg,rgba(255,255,255,0) 0%,#d9dcdf 45%,#c3c7cb 70%,rgba(240,241,242,0) 100%)}

  .headline{position:absolute;color:var(--sky-blue);font-weight:700;letter-spacing:0.2px}
  .subhead{position:absolute;font-weight:400;color:var(--ink-soft)}
  .mistakes{position:absolute;list-style:none;font-weight:500;color:var(--ink)}
  .mistakes li{display:flex;align-items:center}
  .mistakes svg{flex:none}

  .brand{position:absolute;display:flex;align-items:center}
  .brand-mark{background:var(--navy);flex:none}
  .brand-name{font-weight:600;color:var(--navy);line-height:1}
  .brand-tag{color:var(--sky-blue);font-weight:500;letter-spacing:0.3px;white-space:nowrap}

  .cta{position:absolute;display:flex;align-items:center;justify-content:center;
    background:linear-gradient(180deg,var(--btn-top),var(--btn-bottom));
    color:#fff;font-weight:400;border:2px solid #fff;border-radius:5px;
    box-shadow:2px 3px 5px rgba(0,0,0,0.35);letter-spacing:0.6px;white-space:nowrap}

  /* Medium rectangle */
  .ad-rect{left:66px;top:265px;width:484px;height:403px}
  .ad-rect .sketch{left:50px;top:8px;width:390px;height:176px}
  .ad-rect .headline{left:35px;top:187px;font-size:32px}
  .ad-rect .subhead{left:35px;top:237px;font-size:17px}
  .ad-rect .mistakes{left:35px;top:272px;font-size:16px}
  .ad-rect .mistakes li{height:26px;gap:6px}
  .ad-rect .brand{left:275px;top:281px;gap:8px}
  .ad-rect .brand-mark{width:34px;height:30px}
  .ad-rect .brand-name{font-size:18px}
  .ad-rect .brand-tag{font-size:4.5px;margin-top:2px}
  .ad-rect .cta{left:257px;top:331px;width:202px;height:32px;font-size:15px}
  .ad-rect .base-band{position:absolute;left:0;bottom:0;width:100%;height:10px;background:var(--sky-blue)}

  /* Half page */
  .ad-tall{left:599px;top:40px;width:484px;height:968px}
  .ad-tall .sketch{left:0;top:30px;width:484px;height:240px}
  .ad-tall .brand{left:67px;top:307px;gap:22px}
  .ad-tall .brand-mark{width:77px;height:65px}
  .ad-tall .brand-name{font-size:39px}
  .ad-tall .brand-tag{font-size:10px;margin-top:6px}
  .ad-tall .headline{left:45px;top:437px;font-size:62px;line-height:64px}
  .ad-tall .subhead{left:45px;top:586px;font-size:26px}
  .ad-tall .mistakes{left:44px;top:640px;font-size:25px}
  .ad-tall .mistakes li{height:38px;gap:10px}
  .ad-tall .cta{left:78px;top:853px;width:330px;height:51px;font-size:26px}
</style>
</head>
<body>

<div class="size-label" style="left:601px;top:16px">300X600px</div>
<div class="size-label" style="left:459px;top:675px">300X250px</div>

<section class="ad ad-rect" aria-label="Medium rectangle ad">
  <div class="sketch" role="img" aria-label="Pencil sketch of a modern two-storey house with trees"></div>
  <h1 class="headline">Planning A New Build?</h1>
  <p class="subhead">Avoid These Common Mistakes:</p>
  <ul class="mistakes">
    <li><svg width="18" height="18" viewBox="0 0 20 20"><path d="M3 3 L17 17 M17 3 L3 17" stroke="var(--cross)" stroke-width="3" stroke-linecap="round"/></svg>Hidden Exclusions</li>
    <li><svg width="18" height="18" viewBox="0 0 20 20"><path d="M3 3 L17 17 M17 3 L3 17" stroke="var(--cross)" stroke-width="3" stroke-linecap="round"/></svg>Missing Scope</li>
    <li><svg width="18" height="18" viewBox="0 0 20 20"><path d="M3 3 L17 17 M17 3 L3 17" stroke="var(--cross)" stroke-width="3" stroke-linecap="round"/></svg>Unrealistic Allowances</li>
    <li><svg width="18" height="18" viewBox="0 0 20 20"><path d="M3 3 L17 17 M17 3 L3 17" stroke="var(--cross)" stroke-width="3" stroke-linecap="round"/></svg>Budget Blowouts</li>
  </ul>
  <div class="brand">
    <span class="brand-mark"></span>
    <div>
      <div class="brand-name">Stone Well</div>
      <div class="brand-tag">COMPARE QUOTES FROM TRUSTED BUILDERS</div>
    </div>
  </div>
  <div class="cta">Download FREE Guide</div>
  <div class="base-band"></div>
</section>

<section class="ad ad-tall" aria-label="Half page ad">
  <div class="sketch" role="img" aria-label="Pencil sketch of a modern two-storey house with trees"></div>
  <div class="brand">
    <span class="brand-mark"></span>
    <div>
      <div class="brand-name">Stone Well</div>
      <div class="brand-tag">COMPARE QUOTES FROM TRUSTED BUILDERS</div>
    </div>
  </div>
  <h1 class="headline">Planning A<br>New Build?</h1>
  <p class="subhead">Avoid These Common Mistakes:</p>
  <ul class="mistakes">
    <li><svg width="30" height="30" viewBox="0 0 20 20"><path d="M3 3 L17 17 M17 3 L3 17" stroke="var(--cross)" stroke-width="3" stroke-linecap="round"/></svg>Hidden Exclusions</li>
    <li><svg width="30" height="30" viewBox="0 0 20 20"><path d="M3 3 L17 17 M17 3 L3 17" stroke="var(--cross)" stroke-width="3" stroke-linecap="round"/></svg>Missing Scope</li>
    <li><svg width="30" height="30" viewBox="0 0 20 20"><path d="M3 3 L17 17 M17 3 L3 17" stroke="var(--cross)" stroke-width="3" stroke-linecap="round"/></svg>Unrealistic Allowances</li>
    <li><svg width="30" height="30" viewBox="0 0 20 20"><path d="M3 3 L17 17 M17 3 L3 17" stroke="var(--cross)" stroke-width="3" stroke-linecap="round"/></svg>Budget Blowouts</li>
  </ul>
  <div class="cta">Download FREE Guide</div>
</section>

</body>
</html>
```